We are in search of a new business card design for our business. We have a Mexican Grocery Store called Tamarindo Market, we would like to see that some have mexican design, but we are open to any type of designs.

Phone: to be announced
Fax: to be announced

Address is:
2465 Calloway Blvd
Dundalk, MD 21222

Industry/Entity Type

Business

```html
<!DOCTYPE html>
<html lang="en">
<head>
<meta charset="utf-8">
<title>Tamarindo Market – Business Card</title>
<link rel="stylesheet" href="https://fonts.googleapis.com/css2?family=Source+Sans+3:wght@400;600;700;800&display=swap">
<style>
  :root {
    --page-bg: #ece8e3;
    --card-white: #ffffff;
    --brand-red: #c4232a;
    --deep-red: #8e1d22;
    --name-red: #8a1f24;
    --title-orange: #f08a12;
    --accent-yellow: #f7b900;
    --accent-green: #3b8d22;
    --ink: #4a4a4a;
    --divider: #bdbdbd;
  }
  * { margin: 0; padding: 0; box-sizing: border-box; }
  html, body { width: 1200px; height: 987px; overflow: hidden; }
  body {
    background: var(--page-bg);
    font-family: "Source Sans 3", "Open Sans", sans-serif;
    position: relative;
  }
  .card {
    position: absolute;
    left: 293px;
    width: 615px;
    height: 351px;
    overflow: hidden;
  }
  .card--front { top: 130px; background: var(--card-white); }
  .card--back {
    top: 506px;
    background: radial-gradient(ellipse at 50% 50%, var(--brand-red) 0%, #b0242a 55%, var(--deep-red) 100%);
    display: flex; align-items: center; justify-content: center;
  }

  /* Brand name lockup: one colour, one weight, one plain circle */
  .brand {
    display: flex; flex-direction: column; align-items: center;
    font-weight: 800; text-align: center; line-height: 1;
  }
  .brand__dot {
    width: 26px; height: 26px; border-radius: 50%;
    margin-bottom: 12px;
  }
  .brand__word { font-size: 62px; letter-spacing: -0.5px; }
  .brand__sub {
    font-size: 22px; letter-spacing: 10px; margin-top: 8px;
    padding-left: 10px;
  }
  .card--front .brand {
    position: absolute; top: 34px; left: 0; right: 0;
    color: var(--brand-red);
  }
  .card--front .brand__dot { background: var(--accent-green); }
  .card--back .brand { color: #ffffff; }
  .card--back .brand__word { font-size: 68px; }
  .card--back .brand__sub { font-size: 24px; }
  .card--back .brand__dot { background: var(--accent-green); }

  .contact {
    position: absolute; top: 265px; left: 37px; right: 20px; height: 48px;
    display: flex; align-items: center;
  }
  .contact__person { width: 168px; }
  .contact__name { color: var(--name-red); font-size: 22px; font-weight: 600; line-height: 1.1; }
  .contact__title { color: var(--title-orange); font-size: 17px; line-height: 1.3; }
  .contact__divider { width: 1px; height: 48px; background: var(--divider); }
  .contact__lines { padding: 0 0 0 30px; width: 188px; }
  .contact__address { padding-left: 24px; }
  .contact__line {
    display: flex; align-items: center; gap: 8px;
    color: var(--ink); font-size: 16px; line-height: 23px;
  }
  .contact__line svg { width: 16px; height: 16px; fill: var(--name-red); }

  .card__stripe {
    position: absolute; left: 0; bottom: 0; width: 615px; height: 11px;
  }
</style>
</head>
<body>
  <section class="card card--front" aria-label="Business card front">
    <div class="brand">
      <span class="brand__dot"></span>
      <span class="brand__word">Tamarindo</span>
      <span class="brand__sub">MARKET</span>
    </div>

    <div class="contact">
      <div class="contact__person">
        <p class="contact__name">LUIS MORENO</p>
        <p class="contact__title">CEO/Founder</p>
      </div>
      <div class="contact__divider"></div>
      <div class="contact__lines">
        <p class="contact__line">
          <svg viewBox="0 0 16 16" aria-hidden="true"><path d="M3.5 1.5l2.5 0 1.3 3.3-1.7 1.2c.8 1.8 2.2 3.2 4 4l1.2-1.7 3.3 1.3v2.5c0 .8-.7 1.4-1.5 1.4C7 13.5 2.5 9 2.1 3c0-.8.6-1.5 1.4-1.5z"/></svg>
          410 555 0187
        </p>
        <p class="contact__line">
          <svg viewBox="0 0 16 16" aria-hidden="true"><path d="M4 1h6l2 2v3H4z M1 7h14v6h-3v2H4v-2H1z M5 11v3h6v-3z"/></svg>
          410 555 0192
        </p>
      </div>
      <div class="contact__divider"></div>
      <div class="contact__address">
        <p class="contact__line">2465 Calloway Blvd</p>
        <p class="contact__line">Dundalk, MD 21222</p>
      </div>
    </div>

    <svg class="card__stripe" viewBox="0 0 615 11" preserveAspectRatio="none" aria-hidden="true">
      <rect width="615" height="11" fill="var(--brand-red)"/>
      <polygon points="432,0 470,0 466,11 428,11" fill="var(--accent-yellow)"/>
      <polygon points="470,0 474,0 470,11 466,11" fill="#ffffff"/>
      <polygon points="474,0 546,0 542,11 470,11" fill="var(--accent-green)"/>
      <polygon points="546,0 550,0 546,11 542,11" fill="#ffffff"/>
    </svg>
  </section>

  <section class="card card--back" aria-label="Business card back">
    <div class="brand">
      <span class="brand__dot"></span>
      <span class="brand__word">Tamarindo</span>
      <span class="brand__sub">MARKET</span>
    </div>
  </section>
</body>
</html>
```